Online Digital Solutions Agency needs a New Business Card

We are a Online/Digital solution agency. We provide WordPress Solutions, Online & Digital Marketing Solutions including SEO, Social Media Marketing and Managed Hosting including VPS and Cloud Hosting solutions. We also design and build bespoke web sites and web applications for various clients. We are very good at site migrations, 3rd party API integrations and mobile app development.

We are rebranding our agency and have already designed a new logo. We have selected 5-6 colours as our base colour and are currently building our new website based around these colour scheme.

Our logo indicates that we are a cloud solution providers, and (i.e. the Clouds), and developers (i.e. HTML Tags, and CSS formats). We use the 5-6 base colours and use various shades of these colours as required.

Our old website is located at: www.brambleforgelabs.com

And our new website is going to be at (we are working on it at the moment ...):
https://creative.brambleforgelabs.co.uk/

Our slogan is "Digital Transformation Specialist"

What we mean by that is; we can take any existing business and get them up and transform them in to the digital world, starting with Hosting, Web Design, Development & Online Marketing aspects.

The powerpoint is a document that we use to present our projects to clients at the moment, and the cloud is on the background as we clarified earlier. (Just to get the idea)

What we are looking for is a Great WoW factor design to start with, ideally with the Logo and Logo colour scheme if possible but not required as long as the designers can do better, and basically give life to our logo and company via the Business card design.

Ideally with some icons perhaps to indicate the address, location, mobile, email, and website would be good but again optional as long as there is a good design.

The cloud can be used as a background if required in a light shade or as a watermark share perhaps.

The logos' and the Illustrator files are shared with you so you can use them as required.

Ideally the business card should have a Name, title, Mobile, Email , Website, Address and perhaps some social media links.

Target Market(s)

New Startups, SME's, Contract and Outsource Clients

Contact Information for Business Card

Company Name:
==============
BrambleForge Labs (UK) Ltd.

Tag Line:
========
“Digital Transformation Specialists”

Adress:
=======

Suite KR73054
14-16 Ashgrove Lane
London
E9 4PD.

Name:
=====
Idris Malek

Title: (Optional)
=============
FQTA, PgD (RNOM)

Role:
=====
Digital Solutions Architect

Email:
=====
idris@brambleforgelabs.uk

WebSite:
=======
http://www.brambleforgelabs.uk

OR

www.brambleforgelabs.uk

Mobile:
======
0044 (0)75 218 30479

OR

+44 (0)75 218 30479

LinkedIN: (Optional)
========
https://uk.linkedin.com/in/idrismalek

Skype: (Optional)
======
idris.malek

Twitter (Optional) : idrismalek

Font styles to use
Serif
Sans Serif

Requirements
Must have
• The Logo
• Business Name
• Person Name
• Title
• Mobile
• Email
• Website
• Address
• I have provided the colour scheme on my files.
Nice to have
• Twiter
• Linked in
• Facebook

```html
<!DOCTYPE html>
<html lang="en">
<head>
<meta charset="utf-8">
<title>BrambleForge Labs – Business Card</title>
<link rel="stylesheet" href="https://fonts.googleapis.com/css2?family=Rubik:wght@500;600&family=Roboto:wght@400&display=swap">
<style>
  :root {
    --bg: #e8e6e1;
    --card: #fdfdfd;
    --navy: #1a5ca8;
    --cyan: #17b2d4;
    --sky: #2a8bd0;
    --ink: #454545;
    --icon: #1f6db8;
  }
  * { margin: 0; padding: 0; box-sizing: border-box; }
  html, body { width: 1200px; height: 1200px; overflow: hidden; }
  body { background: var(--bg); position: relative; font-family: "Roboto", Arial, sans-serif; }

  .card {
    position: absolute; left: 208px; width: 784px; height: 449px;
    background: var(--card);
    box-shadow: 0 3px 8px rgba(0,0,0,.22);
  }
  .card--front { top: 107px; }
  .card--back { top: 645px; height: 447px; }

  .brand {
    position: absolute; display: flex; align-items: center; gap: 12px;
    font-family: "Rubik", Arial, sans-serif; font-weight: 600; color: var(--navy);
    white-space: nowrap;
  }
  .brand__dot { border-radius: 50%; background: var(--cyan); flex: none; }
  .card--front .brand { left: 50px; top: 112px; font-size: 36px; }
  .card--front .brand__dot { width: 28px; height: 28px; }
  .card--back .brand { left: 0; right: 0; justify-content: center; top: 180px; font-size: 52px; gap: 16px; }
  .card--back .brand__dot { width: 42px; height: 42px; }

  .person { position: absolute; right: 48px; top: 78px; text-align: right; }
  .person__name { font-family: "Rubik", Arial, sans-serif; font-weight: 500; font-size: 35px; color: var(--navy); line-height: 42px; }
  .person__creds { font-size: 18px; color: var(--ink); margin-top: 2px; line-height: 22px; }
  .person__role { font-size: 19px; color: var(--cyan); line-height: 26px; }

  .contacts { position: absolute; left: 47px; top: 252px; list-style: none; }
  .contacts li { display: flex; align-items: center; gap: 8px; font-size: 19.5px; color: var(--ink); height: 30.3px; }
  .contacts svg { width: 22px; height: 22px; flex: none; }

  .address { position: absolute; right: 48px; top: 349px; text-align: right; font-size: 19px; line-height: 25px; color: var(--ink); font-style: normal; }

  .company { position: absolute; left: 0; right: 0; top: 343px; text-align: center; }
  .company__name { font-size: 19px; color: var(--navy); text-transform: uppercase; line-height: 25px; }
  .company__address { font-size: 19.5px; color: var(--sky); line-height: 25px; }
</style>
</head>
<body>

<section class="card card--front">
  <div class="brand"><span class="brand__dot"></span>BrambleForge Labs</div>

  <div class="person">
    <div class="person__name">Idris Malek</div>
    <div class="person__creds">FQTA, PgD(RNOM)</div>
    <div class="person__role">Digital Solutions Architect</div>
  </div>

  <ul class="contacts">
    <li>
      <svg viewBox="0 0 22 22" aria-hidden="true"><circle cx="11" cy="11" r="10" fill="none" stroke="var(--icon)" stroke-width="1.6"/><rect x="7.5" y="5" width="7" height="12" rx="1.3" fill="none" stroke="var(--icon)" stroke-width="1.5"/><circle cx="11" cy="14.8" r=".9" fill="var(--icon)"/></svg>
      +44 (0)75 218 30479
    </li>
    <li>
      <svg viewBox="0 0 22 22" aria-hidden="true"><circle cx="11" cy="11" r="10" fill="none" stroke="var(--icon)" stroke-width="1.6"/><rect x="5.5" y="7.5" width="11" height="7.5" rx="1" fill="var(--icon)"/><path d="M5.8 8 11 12l5.2-4" fill="none" stroke="#fff" stroke-width="1.1"/></svg>
      idris@brambleforgelabs.uk
    </li>
    <li>
      <svg viewBox="0 0 22 22" aria-hidden="true"><circle cx="11" cy="11" r="10" fill="none" stroke="var(--icon)" stroke-width="1.6"/><circle cx="11" cy="11" r="6" fill="none" stroke="var(--icon)" stroke-width="1.4"/><path d="M5 11h12M11 5c-2.5 3.5-2.5 8.5 0 12M11 5c2.5 3.5 2.5 8.5 0 12" fill="none" stroke="var(--icon)" stroke-width="1.1"/></svg>
      www.brambleforgelabs.uk
    </li>
    <li>
      <svg viewBox="0 0 22 22" aria-hidden="true"><circle cx="11" cy="11" r="10" fill="var(--cyan)"/></svg>
      idris.malek
    </li>
    <li>
      <svg viewBox="0 0 22 22" aria-hidden="true"><circle cx="11" cy="11" r="10" fill="var(--icon)"/></svg>
      uk.profilenest.net/in/idrismalek
    </li>
  </ul>

  <address class="address">
    14-16, Ashgrove Lane London<br>E9 4PD United Kingdom
  </address>
</section>

<section class="card card--back">
  <div class="brand"><span class="brand__dot"></span>BrambleForge Labs</div>
  <div class="company">
    <div class="company__name">BrambleForge Labs (UK) Limited.</div>
    <div class="company__address">14-16 Ashgrove Lane, London, E9 4PD, England, United Kingdom</div>
  </div>
</section>

</body>
</html>
```